Project Management Consultancy needs logo, business card and stationary design

I need a logo, business card and stationary design for a start-up project management consultancy servicing clients in corporate, education, aviation, local government and construction sectors.

The business will provide professional advice to clients and our people, knowledge and experience is essentially what we sell.

Our role is to assist our clients in delivering successful construction and transition projects whilst ensuring that their needs are identified, understood and achieved.

The company is small and provides a tailor made service for our clients. We pride ourselves on being
- professional
- innovative
- collaborative
- dependable
- communicative
- confident
- bold
The logo, business card and stationary should reflect this.

Can you please include the following on the stationary as appropriate.
Address:
17 Merrowind Close
Tarrabin
NSW 2593

ABN: 42 873 306 218

I very much look forward to receiving your designs.

Gareth P.

Target Market(s)

Corporate clients such as: airports, universities, government, financial organisations, etc.

Industry/Entity Type

Management Consulting

Contact Information for Business Card

Gareth Pellow
Director
Pellow Management Consulting Pty Ltd
e. gareth.pellow@pellow-mc.example.com.au
m. +61 455 318 906

Font styles to use
Other font styles liked:
• perhaps Arial Narrow? I am open to suggestions

Requirements
Must have
• An dynamic and corporate look and feel.
Should not have
• Should not be boring.

```html
<!DOCTYPE html>
<html lang="en">
<head>
<meta charset="utf-8">
<title>Pellow Management Consulting – Business Card</title>
<link rel="stylesheet" href="https://fonts.googleapis.com/css2?family=Jost:wght@400;500&display=swap">
<style>
  :root {
    --paper: #ffffff;
    --ink: #111111;
    --rule: #1a1a1a;
  }
  html, body {
    margin: 0;
    padding: 0;
    width: 1200px;
    height: 663px;
    overflow: hidden;
    background: var(--paper);
  }
  .canvas {
    position: relative;
    width: 1200px;
    height: 663px;
    background: var(--paper);
    font-family: "Jost", "Helvetica Neue", Arial, sans-serif;
    color: var(--ink);
  }
  .card {
    position: absolute;
    left: 71px;
    top: 82px;
    width: 1057px;
    height: 499px;
    border: 1.5px solid var(--ink);
    box-sizing: border-box;
  }
  .brand-name {
    position: absolute;
    left: 0;
    right: 0;
    top: 76px;
    margin: 0;
    text-align: center;
    font-size: 20px;
    font-weight: 500;
    line-height: 1.2;
  }
  .holder {
    position: absolute;
    left: 0;
    right: 0;
    top: 364px;
    text-align: center;
  }
  .holder-name {
    margin: 0;
    font-size: 25px;
    font-weight: 500;
    letter-spacing: 3px;
    line-height: 1;
    text-transform: uppercase;
  }
  .holder-role {
    margin: 3px 0 0;
    font-size: 14px;
    font-weight: 500;
    letter-spacing: 1.5px;
    line-height: 1;
    text-transform: uppercase;
  }
  .divider {
    position: absolute;
    left: 102px;
    right: 102px;
    top: 415px;
    height: 0;
    border-top: 2px solid var(--rule);
  }
  .contact {
    position: absolute;
    left: 0;
    right: 0;
    top: 430px;
    text-align: center;
    font-size: 13.5px;
    font-weight: 400;
    line-height: 20px;
  }
  .contact p { margin: 0; }
  .contact .label { font-weight: 500; }
  .contact .sep { padding: 0 5px; }
</style>
</head>
<body>
<div class="canvas">
  <div class="card">
    <p class="brand-name">Pellow Management Consulting</p>

    <div class="holder">
      <h1 class="holder-name">Gareth Pellow</h1>
      <p class="holder-role">Director</p>
    </div>

    <div class="divider"></div>

    <div class="contact">
      <p>Pellow Management Consulting Pty Ltd<span class="sep">|</span>ABN: 42 873 306 218</p>
      <p><span class="label">e.</span> gareth.pellow@pellow-mc.example.com.au<span class="sep">|</span><span class="label">m.</span> +61 455 318 906<span class="sep">|</span>17 Merrowind Close, Tarrabin NSW 2593</p>
    </div>
  </div>
</div>
</body>
</html>
```